Business Card for Graphic Design Firm

This project is for a new graphic design firm based in New Jersey called Velmoth. We outsource graphic design and marketing jobs. We want to communicate that this is a professional company but it as well creative and artistic. This card may be used as a horizontal double sided paper card or a vertical single sided translucent card so feel free to submit designs in whichever format or both.
Updates

Reason: Extending the deadline because I'm not exactly satisfied with the designs so far.

Please view the updated project brief

Target Market(s)

Adults aged 25-60

Industry/Entity Type

Graphic Design

Font styles to use
Serif
Sans Serif

Requirements
Nice to have
• Maybe a triangular pattern around the edges similar to our logo

```html
<!DOCTYPE html>
<html lang="en">
<head>
<meta charset="utf-8">
<title>Velmoth Business Card</title>
<link rel="stylesheet" href="https://fonts.googleapis.com/css2?family=Open+Sans:wght@400;600;700&display=swap">
<style>
  :root {
    --bg: #e9e6e1;
    --card-white: #ffffff;
    --pattern-cream: #f7efdf;
    --band: #f4f4f2;
    --teal: #4aa7bd;
    --orange-text: #f2b33d;
    --grey-mark: #8c9194;
    --card-orange: #ec7f1f;
    --icon-gold: #f0b43a;
    --shadow: rgba(0, 0, 0, 0.18);
  }
  html, body {
    margin: 0;
    padding: 0;
    width: 1200px;
    height: 1023px;
    overflow: hidden;
    background: var(--bg);
    font-family: "Open Sans", Arial, sans-serif;
  }
  .canvas {
    position: relative;
    width: 1200px;
    height: 1023px;
  }
  .card {
    position: absolute;
    box-shadow: 0 10px 30px var(--shadow);
    overflow: hidden;
  }

  /* Front card */
  .card-front {
    left: 70px;
    top: 70px;
    width: 640px;
    height: 366px;
    background: var(--card-white);
  }
  .card-front .pattern {
    position: absolute;
    inset: 0;
    background: linear-gradient(135deg, var(--pattern-cream) 0%, #fbf7ee 50%, var(--pattern-cream) 100%);
  }
  .card-front .band {
    position: absolute;
    left: 0;
    width: 100%;
    height: 14px;
    background: var(--band);
  }
  .band-upper { top: 92px; }
  .band-lower { top: 262px; }
  .holder {
    position: absolute;
    top: 28px;
    left: 0;
    width: 100%;
    text-align: center;
  }
  .holder-name {
    margin: 0;
    font-size: 21px;
    font-weight: 700;
    color: var(--teal);
  }
  .holder-title {
    margin: 2px 0 0;
    font-size: 14px;
    font-weight: 400;
    color: var(--orange-text);
  }
  .brand-front {
    position: absolute;
    left: 80px;
    top: 150px;
    display: flex;
    align-items: center;
    gap: 12px;
  }
  .brand-square {
    width: 34px;
    height: 34px;
    background: var(--teal);
  }
  .brand-name {
    font-size: 40px;
    font-weight: 600;
    letter-spacing: 3px;
    color: var(--grey-mark);
    text-transform: uppercase;
  }
  .contact {
    position: absolute;
    right: 54px;
    top: 132px;
    list-style: none;
    margin: 0;
    padding: 0;
  }
  .contact li {
    display: flex;
    align-items: center;
    justify-content: flex-end;
    gap: 14px;
    font-size: 14px;
    color: var(--teal);
    margin-bottom: 18px;
  }
  .contact svg { width: 16px; height: 16px; }
  .address {
    position: absolute;
    left: 40px;
    bottom: 26px;
    display: flex;
    align-items: center;
    gap: 10px;
    font-size: 14px;
    color: var(--teal);
  }
  .address svg { width: 16px; height: 16px; }

  /* Back card */
  .card-back {
    left: 770px;
    top: 350px;
    width: 366px;
    height: 640px;
    background: var(--card-orange);
    display: flex;
    align-items: center;
    justify-content: center;
  }
  .brand-back {
    display: flex;
    align-items: center;
    gap: 14px;
  }
  .brand-back .brand-square {
    background: var(--grey-mark);
  }
  .brand-back .brand-name {
    font-size: 44px;
  }
</style>
</head>
<body>
<main class="canvas">

  <section class="card card-front" aria-label="Business card front">
    <div class="pattern" role="img" aria-label="Soft cream triangular pattern across the card"></div>
    <div class="band band-upper"></div>
    <div class="band band-lower"></div>

    <header class="holder">
      <h1 class="holder-name">Lena Hartwell</h1>
      <p class="holder-title">Hybrid Clouds</p>
    </header>

    <div class="brand-front">
      <span class="brand-square"></span>
      <span class="brand-name">Velmoth</span>
    </div>

    <ul class="contact">
      <li>
        <span>+41 70 555 12 34</span>
        <svg viewBox="0 0 16 16" aria-hidden="true"><rect x="4" y="1" width="8" height="14" rx="1.5" fill="none" stroke="var(--icon-gold)" stroke-width="1.5"/><circle cx="8" cy="12.5" r="0.9" fill="var(--icon-gold)"/></svg>
      </li>
      <li>
        <span>lena@velmoth.ch</span>
        <svg viewBox="0 0 16 16" aria-hidden="true"><rect x="1" y="3" width="14" height="10" fill="var(--icon-gold)"/><path d="M1 3 L8 9 L15 3" fill="none" stroke="#fff" stroke-width="1.2"/></svg>
      </li>
    </ul>

    <div class="address">
      <svg viewBox="0 0 16 16" aria-hidden="true"><path d="M8 1 L15 8 H13 V15 H9.5 V10.5 H6.5 V15 H3 V8 H1 Z" fill="var(--icon-gold)"/></svg>
      <span>Lindenweg 12 8000 Musterdorf, Switzerland</span>
    </div>
  </section>

  <section class="card card-back" aria-label="Business card back">
    <div class="brand-back">
      <span class="brand-square"></span>
      <span class="brand-name">Velmoth</span>
    </div>
  </section>

</main>
</body>
</html>
```